Redesign wellness clinic website

The project is redesign a wellness clinic http://www.thornleighvitality.example. The new website is to be responsive,clean,bright and a strong call to action which is to book an appointment. The logo will remain the same but the colour scheme on the website should be reflect purple white and green. I want it to be bright and cheerful and the feeling of clarity. The website shouldn't be overloaded with content but more visuals.

Target Market(s)

Anyone that has corporate wellness benefits within the downtown Toronto core. Majority of audience are professional working in Media, Telecommunications and Investments.

Industry/Entity Type

Health And Wellness

Number of Pages Required

5+ page

Font styles to use
Sans Serif

Colors
ffffff
886aae
acd036

Requirements
Must have
• -Strong call to action which is book an appointment like this page https://www.kestrelmotion.example/
• -Services provided icons on the page like https://www.brightpathvitalityhouse.example/
• - Pictures of a good visualizing a fit and healthy life
• - Strong ratings from Quorva, Zintrel, PostMaz, similar to this website http://www.summitbalancehealth.example/our-team-professionals/
• - Bright and clear
Should not have
• -No black and white images (redo our pictures)
• -Dark themes

```html
<!DOCTYPE html>
<html lang="en">
<head>
<meta charset="utf-8">
<title>Thornleigh Vitality Centre</title>
<link href="https://fonts.googleapis.com/css2?family=Alegreya:wght@500;700&family=Open+Sans:ital,wght@0,400;0,600;0,700;1,400&display=swap" rel="stylesheet">
<style>
:root{
  --purple:#7b2a80;
  --green:#a9b934;
  --green-band:#b0bc35;
  --grey-bg:#efefef;
  --badge-fill:#f3f3f3;
  --badge-line:#cfcfcf;
  --text:#555555;
  --heading:#222222;
  --white:#ffffff;
  --serif:"Alegreya", Georgia, serif;
  --sans:"Open Sans", Arial, sans-serif;
}
*{box-sizing:border-box;margin:0;padding:0}
html,body{width:1200px;height:3191px;overflow:hidden}
body{font-family:var(--sans);color:var(--text);background:var(--white);position:relative}
a{color:inherit;text-decoration:none}
.abs{position:absolute}

/* Header */
.site-header{position:absolute;top:0;left:0;width:1200px;height:130px;z-index:3}
.brand{position:absolute;left:64px;top:12px;width:260px;text-align:center;color:var(--purple)}
.brand-dot{width:40px;height:40px;border-radius:50%;border:3px solid var(--green);margin:0 auto 8px}
.brand-name{font-family:var(--sans);font-weight:600;font-size:20px;letter-spacing:-.3px;line-height:1;white-space:nowrap}
.brand-tag{font-size:11px;margin-top:4px}
.contact-bar{position:absolute;right:78px;top:14px;display:flex;align-items:center;gap:8px}
.phone{display:flex;align-items:center;gap:10px;color:var(--purple);font-weight:700;font-size:19px;margin-right:14px}
.social{width:42px;height:42px;border-radius:50%;border:2px solid var(--green);display:block}
.main-nav{position:absolute;right:78px;top:70px;display:flex;gap:26px;font-size:15px;color:#333}
.main-nav .active{color:var(--purple)}

/* Hero */
.hero{position:absolute;top:0;left:0;width:1200px;height:760px;overflow:hidden}
.hero-photo{position:absolute;inset:0;background:linear-gradient(180deg,#eef4f8 0%,#e3eef3 30%,#a9d2dc 48%,#7fbfcc 58%,#cfe3e4 72%,#ece9e2 100%)}
.hero-title{position:absolute;top:276px;width:100%;text-align:center;font-family:var(--serif);font-weight:500;font-size:64px;color:#111}
.btn-book{position:absolute;left:472px;top:374px;width:252px;height:52px;border-radius:26px;background:var(--purple);color:var(--white);font-family:var(--serif);font-weight:700;font-size:20px;display:flex;align-items:center;justify-content:center;box-shadow:0 3px 0 #c7a9c9}
.hero-swoosh{position:absolute;left:0;top:590px;width:1200px;height:170px}

/* Welcome */
.welcome{position:absolute;top:768px;left:0;width:1200px;text-align:center}
.section-title{font-family:var(--serif);font-weight:700;font-size:42px;color:var(--purple);line-height:1.1}
.section-title .accent{color:var(--green)}
.welcome p{width:860px;margin:12px auto 0;font-size:18px;line-height:30px}

/* Services */
.services{position:absolute;top:932px;left:0;width:1200px;height:718px;background:var(--grey-bg)}
.services .section-title{position:absolute;top:34px;width:100%;text-align:center}
.service-hub{position:absolute;left:0;top:0;width:1200px;height:718px}
.service-label{position:absolute;font-family:var(--serif);font-weight:500;font-size:20px;color:var(--heading);line-height:26px}
.service-label.right{text-align:right}

/* Testimonials & Blog */
.columns{position:absolute;top:1690px;left:0;width:1200px;height:400px}
.col-title{position:absolute;top:0;font-family:var(--serif);font-weight:700;font-size:40px;color:var(--purple)}
.col-title .accent{color:var(--green)}
.testimonial{position:absolute;left:79px;display:flex;gap:22px;width:480px}
.avatar{width:64px;height:64px;border-radius:50%;border:3px solid var(--purple);background:radial-gradient(circle at 50% 40%,#f0d8c8,#caa58c);flex:none}
.quote{font-style:italic;font-size:15px;line-height:25px;color:#444}
.client{font-size:15px;color:#333;margin-top:4px}
.post{position:absolute;left:636px;display:flex;gap:18px;width:500px}
.date{width:56px;flex:none;text-align:center;color:var(--white)}
.date .day{background:var(--purple);font-size:28px;font-weight:600;line-height:44px}
.date .mon{background:#5a5a5a;font-size:14px;line-height:24px}
.post h3{font-family:var(--serif);font-weight:500;font-size:17px;color:var(--purple);line-height:22px}
.post p{font-size:15px;line-height:25px;color:#555}

/* Location band */
.location{position:absolute;top:2128px;left:0;width:1200px;height:206px;background:var(--green-band);color:var(--white)}
.location-mark{position:absolute;left:80px;top:36px;width:134px;height:134px;border-radius:50%;border:8px solid var(--white)}
.location h2{position:absolute;left:276px;top:42px;font-family:var(--serif);font-weight:500;font-size:40px}
.location p{position:absolute;left:276px;top:104px;font-size:15px;line-height:24px}
.btn-map{position:absolute;left:936px;top:80px;width:168px;height:46px;border-radius:23px;background:var(--white);color:var(--green-band);font-family:var(--serif);font-weight:700;font-size:18px;display:flex;align-items:center;justify-content:center}

/* Ratings */
.ratings{position:absolute;top:2380px;left:0;width:1200px;height:240px}
.ratings .section-title{position:absolute;top:10px;font-size:40px}
.badge{position:absolute;top:82px;height:134px;border:2px solid var(--badge-line);background:var(--white);display:flex;align-items:center;justify-content:center}
.badge-plain{width:150px;height:90px;border-radius:6px;background:var(--badge-fill)}
.partner-name{font-family:var(--sans);font-weight:600;font-size:26px;color:#1e4f7a;text-align:center;line-height:1.1}

/* Footer */
.footer{position:absolute;top:2640px;left:0;width:1200px;height:488px;background:var(--grey-bg)}
.footer-swoosh{position:absolute;top:0;left:0;width:1200px;height:150px}
.foot-col{position:absolute;top:186px}
.foot-col h4{font-family:var(--serif);font-weight:700;font-size:22px;color:var(--green);margin-bottom:10px}
.foot-col p{font-size:15px;line-height:26px;color:#666}
.read-more{display:inline-block;margin-top:2px;font-size:15px;color:var(--purple);text-decoration:underline}
.tweet{display:flex;gap:12px;margin-bottom:14px;font-size:14px;line-height:22px}
.tweet-dot{width:16px;height:16px;border-radius:50%;background:var(--purple);flex:none;margin-top:3px}
.tweet .handle{color:#666}
.tweet .link{color:var(--purple)}
.tweet .meta{display:flex;justify-content:space-between;width:190px;color:#666}
.video{width:230px;height:138px;background:#111;position:relative}
.video-bar{position:absolute;left:0;bottom:0;width:100%;height:34px;background:#000}
.share-row{display:flex;gap:10px;margin-top:14px}
.share-row span{width:30px;height:30px;background:#7fb4dc;display:block;border-radius:3px}
.share-row span:first-child{background:#777}
.award{width:140px;height:142px;background:linear-gradient(180deg,#f28c2a,#e46d1b);clip-path:polygon(0 0,100% 0,100% 80%,50% 100%,0 80%)}
.award-caption{font-size:14px;line-height:22px;color:var(--white);margin-top:12px;width:210px}
.copyright{position:absolute;left:0;top:3128px;width:1200px;height:63px;background:var(--purple);color:var(--white);font-size:15px;display:flex;align-items:center;justify-content:center}
</style>
</head>
<body>

<section class="hero">
  <div class="hero-photo" role="img" aria-label="Photo of a young woman jogging along a bright beach by the sea"></div>
  <h1 class="hero-title">Many disciplines, one philosophy</h1>
  <a class="btn-book" href="#">BOOK APPOINTMENT</a>
  <svg class="hero-swoosh" viewBox="0 0 1200 170" preserveAspectRatio="none" aria-hidden="true">
    <path d="M420 100 C700 40 1000 20 1200 30 L1200 150 C1050 100 800 85 420 100Z" fill="var(--purple)"/>
    <path d="M0 112 C150 116 300 104 420 100 C800 85 1050 100 1200 150 L1200 170 L0 170Z" fill="#ffffff"/>
  </svg>
</section>

<header class="site-header">
  <div class="brand">
    <div class="brand-dot"></div>
    <div class="brand-name">thornleigh vitality centre</div>
    <div class="brand-tag">many disciplines, one philosophy</div>
  </div>
  <div class="contact-bar">
    <div class="phone">
      <svg width="18" height="18" viewBox="0 0 24 24" aria-hidden="true"><path fill="var(--purple)" d="M6.6 10.8a15.1 15.1 0 0 0 6.6 6.6l2.2-2.2c.3-.3.7-.4 1-.2 1.1.4 2.3.6 3.6.6.6 0 1 .4 1 1V20c0 .6-.4 1-1 1C10.6 21 3 13.4 3 4c0-.6.4-1 1-1h3.5c.6 0 1 .4 1 1 0 1.3.2 2.5.6 3.6.1.3 0 .7-.2 1z"/></svg>
      416-555-0142
    </div>
    <a class="social" href="#" aria-label="Social profile 1"></a>
    <a class="social" href="#" aria-label="Social profile 2"></a>
    <a class="social" href="#" aria-label="Social profile 3"></a>
    <a class="social" href="#" aria-label="Social profile 4"></a>
  </div>
  <nav class="main-nav">
    <a class="active" href="#">Home</a>
    <a href="#">Fees and Services</a>
    <a href="#">Our Staff</a>
    <a href="#">News and Updates</a>
    <a href="#">Corporate Wellness</a>
    <a href="#">Forms</a>
    <a href="#">Contact</a>
  </nav>
</header>

<section class="welcome">
  <h2 class="section-title"><span class="accent">Welcome to</span> thornleigh vitality center</h2>
  <p>Our Centre is committed to helping improve and extend the lives of as many people as possible in our community. Come and join our Family and start changing your life today.</p>
</section>

<section class="services">
  <h2 class="section-title"><span class="accent">Our</span> Best Services</h2>
  <svg class="service-hub" viewBox="0 0 1200 718" aria-hidden="true">
    <circle cx="600" cy="334" r="182" fill="#e4e4e4"/>
    <circle cx="600" cy="334" r="150" fill="#d6d6d6"/>
    <circle cx="600" cy="338" r="124" fill="#c9c9c9" opacity=".6"/>
    <circle cx="600" cy="334" r="120" fill="#f4f4f4"/>
    <circle cx="600" cy="334" r="112" fill="none" stroke="#e8e8e8" stroke-width="2"/>
    <g fill="#ffffff" stroke="var(--green)" stroke-width="3">
      <circle cx="462" cy="166" r="48"/>
      <circle cx="736" cy="166" r="48"/>
      <circle cx="385" cy="313" r="48"/>
      <circle cx="813" cy="313" r="48"/>
      <circle cx="434" cy="477" r="48"/>
      <circle cx="766" cy="477" r="48"/>
      <circle cx="600" cy="553" r="48"/>
    </g>
    <g fill="none" stroke="var(--purple)" stroke-width="3" stroke-linecap="round" stroke-linejoin="round">
      <path d="M462 144v44M448 156h28M452 176h20"/>
      <path d="M716 172c8-8 14 8 22 0s14 8 22 0M716 160c8-8 14 8 22 0s14 8 22 0"/>
      <path d="M385 295v36M367 313h36"/>
      <ellipse cx="808" cy="318" rx="9" ry="16"/><circle cx="822" cy="298" r="4"/>
      <circle cx="428" cy="457" r="5"/><path d="M428 465v16h16l6 14M420 472a14 14 0 1 0 18 20"/>
      <path d="M754 497l6-8M762 487l6-8M770 477l6-8M778 467l6-8"/>
      <path d="M600 573c-22-14-28-26-20-36 6-7 14-5 20 3 6-8 14-10 20-3 8 10 2 22-20 36z"/><path d="M576 553h12l5-9 7 18 5-9h19"/>
    </g>
  </svg>
  <div class="service-label right" style="left:180px;top:156px;width:206px">Chiropractic</div>
  <div class="service-label" style="left:812px;top:156px">Massage Therapy</div>
  <div class="service-label right" style="left:100px;top:302px;width:202px">Physiotherapy</div>
  <div class="service-label" style="left:894px;top:302px">Chiropody</div>
  <div class="service-label right" style="left:100px;top:467px;width:252px">Active Rehabilitation</div>
  <div class="service-label" style="left:842px;top:467px">Osteopathy</div>
  <div class="service-label" style="left:480px;top:614px;width:240px;text-align:center">Nutrition and Lifestyle Medicine</div>
</section>

<section class="columns">
  <h2 class="col-title" style="left:79px">Client <span class="accent">Testimonials</span></h2>
  <h2 class="col-title" style="left:636px"><span class="accent">Latest</span> Blog</h2>

  <div class="testimonial" style="top:72px">
    <div class="avatar" role="img" aria-label="Client portrait"></div>
    <div><p class="quote">Lorem Ipsum is simply dummy text of the printing and typesetting industry.</p><p class="client">- Client Name</p></div>
  </div>
  <div class="testimonial" style="top:186px">
    <div class="avatar" role="img" aria-label="Client portrait"></div>
    <div><p class="quote">Lorem Ipsum is simply dummy text of the printing and typesetting industry.</p><p class="client">- Client Name</p></div>
  </div>
  <div class="testimonial" style="top:296px">
    <div class="avatar" role="img" aria-label="Client portrait"></div>
    <div><p class="quote">Lorem Ipsum is simply dummy text of the printing and typesetting industry.</p><p class="client">- Client Name</p></div>
  </div>

  <article class="post" style="top:72px">
    <div class="date"><div class="day">21</div><div class="mon">mar</div></div>
    <div><h3>Lorem Ipsum is simply dummy.</h3><p>Lorem Ipsum is simply dummy text of the printing and typesetting industry. Lorem Ipsum has been.</p></div>
  </article>
  <article class="post" style="top:186px">
    <div class="date"><div class="day">21</div><div class="mon">mar</div></div>
    <div><h3>Lorem Ipsum is simply dummy.</h3><p>Lorem Ipsum is simply dummy text of the printing and typesetting industry. Lorem Ipsum has been.</p></div>
  </article>
  <article class="post" style="top:290px">
    <div class="date"><div class="day">21</div><div class="mon">mar</div></div>
    <div><h3>Lorem Ipsum is simply dummy.</h3><p>Lorem Ipsum is simply dummy text of the printing and typesetting industry. Lorem Ipsum has been.</p></div>
  </article>
</section>

<section class="location">
  <div class="location-mark" aria-hidden="true"></div>
  <h2>Visit our new location</h2>
  <p>We are open for business at 7:30 am. Open 7 days a week!<br>Ask one of our associates about our Referral Reward Program!</p>
  <a class="btn-map" href="#">SEE MAP</a>
</section>

<section class="ratings">
  <h2 class="section-title" style="left:120px"><span class="accent">Strong</span> Ratings From</h2>
  <h2 class="section-title" style="left:877px"><span class="accent">Our</span> Partner</h2>
  <div class="badge" style="left:121px;width:205px" role="img" aria-label="Zintrel reviews badge"><div class="badge-plain"></div></div>
  <div class="badge" style="left:366px;width:204px" role="img" aria-label="Quorva rating badge"><div class="badge-plain"></div></div>
  <div class="badge" style="left:611px;width:204px" role="img" aria-label="Top rated clinic badge"><div class="badge-plain"></div></div>
  <div class="badge" style="left:877px;width:208px">
    <div class="partner-name">Merrow<br>Dental Studio</div>
  </div>
</section>

<footer class="footer">
  <svg class="footer-swoosh" viewBox="0 0 1200 150" preserveAspectRatio="none" aria-hidden="true">
    <path d="M0 0 H1200 V0 C1100 60 900 90 420 60 C250 48 100 30 0 20Z" fill="#ffffff"/>
    <path d="M420 60 C900 90 1100 60 1200 0 L1200 40 C1080 120 800 130 420 60Z" fill="var(--purple)"/>
  </svg>
  <div class="foot-col" style="left:79px;width:210px">
    <h4>About us</h4>
    <p>stablished in 1989 the Thornleigh Vitality Centre has become one of Canada's leaders in providing quality care and innovative wellness programs for the community...</p>
    <a class="read-more" href="#">READ MORE</a>
  </div>
  <div class="foot-col" style="left:347px;width:230px">
    <h4>Our Tweets</h4>
    <div class="tweet"><span class="tweet-dot"></span><div><div class="handle">@thornleighvital</div><div class="link">tv.example/8qw68D5Rf</div><div class="meta"><span>♡ ↦</span><span>4 days ago</span></div></div></div>
    <div class="tweet"><span class="tweet-dot"></span><div><div class="handle">@thornleighvital</div><div class="link">tv.example/8qw68D5Rf</div><div class="meta"><span>♡ ↦</span><span>4 days ago</span></div></div></div>
  </div>
  <div class="foot-col" style="left:615px;width:240px">
    <h4>Video Review</h4>
    <div class="video" role="img" aria-label="Embedded client video review">
      <svg class="abs" style="left:95px;top:34px" width="40" height="40" viewBox="0 0 40 40" aria-hidden="true"><circle cx="20" cy="20" r="19" fill="#333"/><path d="M16 12l12 8-12 8z" fill="#fff"/></svg>
      <div class="video-bar">
        <svg width="230" height="34" viewBox="0 0 230 34" aria-hidden="true"><path d="M10 11l10 6-10 6z" fill="#fff"/><circle cx="36" cy="17" r="5" fill="#fff"/><rect x="44" y="16" width="60" height="2" fill="#777"/><text x="118" y="21" fill="#fff" font-size="11" font-family="Open Sans, sans-serif">0:00</text><path d="M166 14h4l5-4v14l-5-4h-4z" fill="#fff"/><path d="M200 11h5M200 11v5M214 23h-5M214 23v-5" stroke="#fff" stroke-width="2"/></svg>
      </div>
    </div>
    <div class="share-row"><span aria-label="Share link"></span><span aria-label="Share link"></span></div>
  </div>
  <div class="foot-col" style="left:885px;width:230px">
    <h4>Award</h4>
    <div class="award" role="img" aria-label="Community choice award badge"></div>
    <p class="award-caption">Voted a top community choice wellness centre in Toronto</p>
  </div>
</footer>

<div class="copyright">©thornleigh vitality center. 2017 - All Rights Reserved.</div>

</body>
</html>
```